New singe page website for our software development company

We need a single webpage that includes information about our company, contact details and a job posting. It should scroll vertically with some cool animations and parallax scrolling effects.

We are a software development consulting company that writes custom software for our customers. The webpage should have graphics and illustrations that illustrate this.

Find our logo attached, it can be modified as needed.

Thanks for all the design. When looking through the various design it's clear to us, that car related images does not look right.

We got to have software design/engineering images instead.

Our unique selling points are:

• Custom software development
• Project Managment
• Industry Services
We want these displayed with some text and icons. The icons should either have the red/brown colour from our logo, or a colour that matches the design

Software

```html
<!DOCTYPE html>
<html lang="en">
<head>
<meta charset="utf-8">
<title>Brightwell – Software Development Consulting</title>
<link href="https://fonts.googleapis.com/css2?family=Exo+2:wght@400;500&family=Ubuntu:wght@300;400;500&display=swap" rel="stylesheet">
<style>
:root{
  --brand:#8a2a14;
  --brand-dark:#7a1f0f;
  --brand-btn:#c4401d;
  --apply:#9c4a32;
  --apply-hot:#e8141b;
  --blue:#1a6fb8;
  --text:#555;
  --muted:#8a8a8a;
  --row:#eef4fa;
  --side:#f3f3f3;
  --line:#dcdcdc;
  --load:#efe3df;
  --foot:#2b2b2b;
  --green:#5cb82a;
}
*{box-sizing:border-box;margin:0;padding:0}
html,body{width:927px;height:1200px;overflow:hidden;background:#fff}
body{font-family:"Ubuntu",sans-serif;color:var(--text)}
.canvas{position:relative;width:927px;height:1200px;overflow:hidden}
.abs{position:absolute}

/* header */
.site-header{position:absolute;left:0;top:0;width:927px;height:56px;background:#fff;border-bottom:1px solid #e6e6e6}
.brand{position:absolute;left:132px;top:16px;font-family:"Exo 2",sans-serif;font-size:20px;color:var(--brand)}
.nav a{position:absolute;top:19px;font-size:12px;color:#444;text-decoration:none}
.nav .active{color:var(--blue);border-bottom:1px solid var(--blue);padding-bottom:2px}
.search{position:absolute;left:661px;top:17px;width:134px;height:23px;border:1px solid #ddd;border-radius:2px;font-size:8px;color:#999;padding:8px 0 0 9px}
.search svg{position:absolute;right:10px;top:6px}

/* hero */
.hero{position:absolute;left:0;top:56px;width:927px;height:384px;background:linear-gradient(160deg,#6f6c68 0%,#4b4a48 45%,#5f5650 70%,#3c3a39 100%)}
.hero-title{position:absolute;left:0;width:927px;top:96px;text-align:center;font-family:"Exo 2",sans-serif;font-size:58px;color:#fff;letter-spacing:1px}
.hero-sub{position:absolute;left:0;width:927px;top:158px;text-align:center;font-size:17px;font-weight:300;color:#fff}
.hero-rule{position:absolute;left:284px;top:190px;width:358px;height:1px;background:rgba(255,255,255,.45)}
.hero-text{position:absolute;left:0;width:927px;top:202px;text-align:center;font-size:12.5px;line-height:16px;color:#fff;font-weight:300}
.hero-btn{position:absolute;left:409px;top:246px;width:109px;height:32px;background:var(--blue);color:#fff;font-size:15px;font-weight:500;text-align:center;line-height:32px}
.hero-dot{position:absolute;left:762px;top:17px;width:20px;height:20px;border-radius:50%;border:2px solid #fff;background:#1c5f9e}

/* sidebar */
.sidebar{position:absolute;left:0;top:440px;width:294px;height:552px;background:var(--side);border-right:1px solid #e2e2e2}
.side-title{position:absolute;left:132px;font-family:"Exo 2",sans-serif;color:var(--brand)}
.side-text{position:absolute;left:133px;width:148px;font-size:9.8px;line-height:12.6px;color:#777;font-weight:300}
.side-rule{position:absolute;left:132px;width:162px;height:1px;background:#d6d6d6}
.feedback{position:absolute;left:133px;top:250px;width:146px;height:91px;background:var(--brand-dark)}
.feedback p{position:absolute;left:6px;top:14px;font-size:8.6px;line-height:12.6px;color:#fff}
.feedback-btn{position:absolute;left:7px;top:48px;width:133px;height:28px;background:var(--brand-btn);color:#fff;font-size:10px}
.feedback-btn span{position:absolute;left:48px;top:8px}
.feedback-btn i{position:absolute;left:34px;top:0;width:1px;height:28px;background:rgba(0,0,0,.2)}
.quote-name{position:absolute;left:120px;top:480px;width:104px;text-align:right;font-size:9.5px;color:var(--brand)}
.quote-role{position:absolute;left:120px;top:491px;width:104px;text-align:right;font-size:8px;color:var(--muted)}
.avatar{position:absolute;left:244px;top:473px;width:34px;height:34px;border-radius:50%;background:linear-gradient(135deg,#6b5647,#2f2a26);border:2px solid #fff}
.quote-split{position:absolute;left:234px;top:470px;width:1px;height:40px;background:#ddd}

/* services */
.service{position:absolute;top:477px;height:79px;border:1px solid #dcdcdc;background:linear-gradient(#fff,#f4f4f4)}
.service span{position:absolute;left:54px;top:28px;font-size:11px;line-height:12.5px;color:#555}
.service.is-active span{color:var(--blue)}
.service svg{position:absolute;left:10px;top:18px}

/* jobs */
.jobs-title{position:absolute;left:314px;top:592px;font-family:"Exo 2",sans-serif;font-size:21px;color:var(--blue)}
.jobs-sub{position:absolute;left:315px;top:621px;font-size:10.5px;color:var(--brand)}
.job{position:absolute;left:314px;width:480px}
.job.alt{background:var(--row)}
.job .star{position:absolute;left:11px}
.job h3{position:absolute;left:32px;font-size:11px;font-weight:300;color:#555}
.job .where{position:absolute;left:32px;font-size:9.2px;color:var(--blue)}
.job .loc,.job .date{position:absolute;font-size:9.2px;color:var(--muted)}
.job .loc{left:266px}
.job .date{left:336px}
.job .apply{position:absolute;left:387px;width:73px;height:18px;background:var(--apply);color:#fff;font-size:10.5px;text-align:center;line-height:18px}
.job .apply.hot{background:var(--apply-hot)}
.load-more{position:absolute;left:314px;top:884px;width:481px;height:38px;background:var(--load);color:#8a3a22;font-size:12.5px;text-align:center;line-height:38px}
.to-top{position:absolute;left:826px;top:956px;width:36px;height:36px;background:var(--blue)}

/* footer */
.footer{position:absolute;left:0;top:992px;width:927px;height:208px;background:var(--foot)}
.footer-map{position:absolute;left:0;top:0;width:927px;height:208px;background:radial-gradient(ellipse at 75% 40%,#3a3a3a,#262626 70%)}
.foot-title{position:absolute;top:42px;font-family:"Exo 2",sans-serif;font-size:19px;color:#fff}
.field{position:absolute;background:#fff;border:1px solid #ccc;font-size:8.5px;color:#888}
.send{position:absolute;left:486px;top:1069px;width:86px;height:57px;background:var(--green);color:#fff;font-family:"Exo 2",sans-serif;font-size:22px;text-align:center;line-height:57px;border:1px solid #7cd14a}
.addr{position:absolute;left:614px;font-size:13px;color:#fff}
.addr svg{position:absolute;left:0;top:1px}
.addr span{position:absolute;left:20px;top:0;white-space:nowrap}
.foot-rule{position:absolute;left:0;top:1158px;width:927px;height:1px;background:#1a1a1a;border-bottom:1px solid #3a3a3a}
.copyright{position:absolute;left:0;top:1173px;width:927px;text-align:center;font-size:9px;color:#ddd}
</style>
</head>
<body>
<div class="canvas">

  <header class="site-header">
    <div class="brand">Brightwell</div>
    <nav class="nav">
      <a class="active" style="left:382px">About Us</a>
      <a style="left:458px">Contact details</a>
      <a style="left:564px">Job posting</a>
    </nav>
    <div class="search">Search
      <svg width="11" height="11" viewBox="0 0 11 11"><circle cx="4.5" cy="4.5" r="3.5" fill="none" stroke="#aaa" stroke-width="1.2"/><path d="M7 7l3 3" stroke="#aaa" stroke-width="1.3"/></svg>
    </div>
  </header>

  <section class="hero" role="img" aria-label="Photo of software consultants working in a bright open-plan office">
    <div class="hero-dot"></div>
    <h1 class="hero-title">Brightwell</h1>
    <div class="hero-sub">Software Development Consulting</div>
    <div class="hero-rule"></div>
    <p class="hero-text">Lorem Ipsum is that it has a more-or-less normal distribution<br>of letters, as opposed to using 'Content here,</p>
    <div class="hero-btn">Read More</div>
  </section>

  <aside class="sidebar">
    <h2 class="side-title" style="top:42px;font-size:19px">Brief</h2>
    <p class="side-text" style="top:74px">There are many variations of passages of Lorem Ipsum available, but the majority have suffered alteration in some form, by injected humour, or randomised words which don't look even slightly believable. If you are going to use a passage of Lorem Ipsum, you need to be sure there isn't anything embarrassing hidden in the middle of text.</p>
    <div class="side-rule" style="top:237px"></div>
    <div class="feedback">
      <p>Please help us to improve we<br>read each and every suggetion</p>
      <div class="feedback-btn">
        <svg class="abs" style="left:11px;top:8px" width="13" height="12" viewBox="0 0 13 12"><path d="M1 4h3l5-3v10L4 8H1z" fill="none" stroke="#fff" stroke-width="1"/></svg>
        <i></i><span>Send Feedback</span>
      </div>
    </div>
    <div class="side-rule" style="top:358px"></div>
    <h2 class="side-title" style="top:383px;font-size:14px">Testimonials</h2>
    <p class="side-text" style="top:404px;font-size:9.8px;line-height:13.3px;width:150px">Working with Kelvo Systems was easy and convenient. Jonas was very helpful and patient in maki ng sure the database was exact ly what we needed..</p>
    <div class="quote-name">Marlene Tovsen</div>
    <div class="quote-role">Sr. Manager</div>
    <div class="quote-split"></div>
    <div class="avatar" role="img" aria-label="Portrait of the client giving the testimonial"></div>
  </aside>

  <div class="service" style="left:314px;width:156px">
    <svg width="42" height="44" viewBox="0 0 42 44"><path d="M4 20l17-6 17 6v18l-17 6-17-6z" fill="#8b8b8b"/><path d="M21 26v18M4 20l17 6 17-6" stroke="#666" fill="none"/><path d="M14 4h14l-3 12H17z" fill="#a9a9a9"/></svg>
    <span>Custom Software<br>Development</span>
  </div>
  <div class="service is-active" style="left:483px;width:149px">
    <svg width="40" height="44" viewBox="0 0 40 44"><rect x="4" y="6" width="32" height="24" fill="none" stroke="#1a6fb8" stroke-width="3"/><rect x="2" y="3" width="36" height="4" fill="#1a6fb8"/><path d="M10 24l7-8 5 5 8-9" stroke="#1a6fb8" stroke-width="2" fill="none"/><path d="M10 30l-4 10M30 30l4 10" stroke="#1a6fb8" stroke-width="3"/></svg>
    <span>Project<br>Managment</span>
  </div>
  <div class="service" style="left:645px;width:149px">
    <svg width="40" height="40" viewBox="0 0 40 40"><circle cx="13" cy="26" r="8" fill="none" stroke="#8b8b8b" stroke-width="5" stroke-dasharray="3 2"/><circle cx="28" cy="12" r="6" fill="none" stroke="#8b8b8b" stroke-width="4" stroke-dasharray="3 2"/></svg>
    <span>Our Industry<br>Services</span>
  </div>

  <h2 class="jobs-title">Showing: All Jobs</h2>
  <p class="jobs-sub">You are viewing All Types of jobs from All States - All Countries</p>

  <div class="job alt" style="top:653px;height:59px">
    <svg class="star" style="top:25px" width="10" height="10" viewBox="0 0 10 10"><path d="M5 0l1.5 3.3 3.5.4-2.6 2.4.7 3.5L5 7.8 1.9 9.6l.7-3.5L0 3.7l3.5-.4z" fill="#bbb"/></svg>
    <h3 style="top:17px">Social Media Expert</h3>
    <div class="where" style="top:33px">Required at Corvana</div>
    <div class="loc" style="top:24px">⚲ Lindeby</div>
    <div class="date" style="top:24px">◌ 21 fab</div>
    <div class="apply hot" style="top:20px">Apply Now</div>
  </div>
  <div class="job" style="top:712px;height:56px">
    <svg class="star" style="top:24px" width="10" height="10" viewBox="0 0 10 10"><path d="M5 0l1.5 3.3 3.5.4-2.6 2.4.7 3.5L5 7.8 1.9 9.6l.7-3.5L0 3.7l3.5-.4z" fill="#bbb"/></svg>
    <h3 style="top:15px">Full time Content Writer</h3>
    <div class="where" style="top:31px">Required at Textmill</div>
    <div class="loc" style="top:23px">⚲ Lindeby</div>
    <div class="date" style="top:23px">◌ 21 fab</div>
    <div class="apply" style="top:20px">Apply Now</div>
  </div>
  <div class="job alt" style="top:768px;height:58px">
    <svg class="star" style="top:25px" width="10" height="10" viewBox="0 0 10 10"><path d="M5 0l1.5 3.3 3.5.4-2.6 2.4.7 3.5L5 7.8 1.9 9.6l.7-3.5L0 3.7l3.5-.4z" fill="#bbb"/></svg>
    <h3 style="top:15px">Social Media Expert</h3>
    <div class="where" style="top:31px">Required at Corvana</div>
    <div class="loc" style="top:23px">⚲ Lindeby</div>
    <div class="date" style="top:23px">◌ 21 fab</div>
    <div class="apply" style="top:20px">Apply Now</div>
  </div>
  <div class="job" style="top:826px;height:58px">
    <svg class="star" style="top:24px" width="10" height="10" viewBox="0 0 10 10"><path d="M5 0l1.5 3.3 3.5.4-2.6 2.4.7 3.5L5 7.8 1.9 9.6l.7-3.5L0 3.7l3.5-.4z" fill="#bbb"/></svg>
    <h3 style="top:15px">Full time Content Writer</h3>
    <div class="where" style="top:31px">Required at Textmill</div>
    <div class="loc" style="top:23px">⚲ Lindeby</div>
    <div class="date" style="top:23px">◌ 21 fab</div>
    <div class="apply" style="top:20px">Apply Now</div>
  </div>
  <div class="load-more">Load Next 35 Jobs</div>

  <div class="to-top"><svg width="36" height="36" viewBox="0 0 36 36"><path d="M10 22l8-8 8 8" fill="none" stroke="#fff" stroke-width="3.5"/></svg></div>

  <footer class="footer">
    <div class="footer-map" role="img" aria-label="Dark street map of the office neighbourhood"></div>
    <h2 class="foot-title" style="left:130px">CONTACT</h2>
    <h2 class="foot-title" style="left:606px">OUR ADDRESS</h2>
  </footer>

  <div class="field" style="left:132px;top:1069px;width:186px;height:27px;padding:9px 0 0 25px">
    <svg class="abs" style="left:10px;top:8px" width="10" height="10" viewBox="0 0 10 10"><circle cx="5" cy="3" r="2.5" fill="#aaa"/><path d="M0 10c0-4 10-4 10 0z" fill="#aaa"/></svg>First Name</div>
  <div class="field" style="left:132px;top:1099px;width:186px;height:27px;padding:9px 0 0 24px">
    <svg class="abs" style="left:10px;top:10px" width="10" height="7" viewBox="0 0 10 7"><rect width="10" height="7" fill="#bbb"/><path d="M0 0l5 4 5-4" stroke="#fff" fill="none"/></svg>Your Email Address</div>
  <div class="field" style="left:326px;top:1069px;width:152px;height:57px;padding:7px 0 0 8px">Your Message</div>
  <div class="send">SEND</div>

  <div class="addr" style="top:1063px">
    <svg width="11" height="14" viewBox="0 0 11 14"><path d="M5.5 0C2.5 0 0 2.3 0 5.3 0 9 5.5 14 5.5 14S11 9 11 5.3C11 2.3 8.5 0 5.5 0z" fill="#fff"/><circle cx="5.5" cy="5.2" r="2" fill="#2b2b2b"/></svg>
    <span>Kvernveien 12b 0391 Lysaker</span></div>
  <div class="addr" style="top:1089px">
    <svg width="12" height="12" viewBox="0 0 12 12"><path d="M2 0l3 3-1.5 2c1 1.5 2 2.5 3.5 3.5L9 7l3 3-2 2C5 11 1 7 0 2z" fill="#fff"/></svg>
    <span>21-60-38-14</span></div>
  <div class="addr" style="top:1113px">
    <svg width="15" height="11" viewBox="0 0 15 11" style="top:3px"><rect width="15" height="11" fill="#fff"/><path d="M0 0l7.5 6L15 0" stroke="#2b2b2b" fill="none"/></svg>
    <span>post@brightwell.no</span></div>

  <div class="foot-rule"></div>
  <div class="copyright">© Copyright 2014 brightwell.no</div>
</div>
</body>
</html>
```